One label design for 3 different sizes of honey bottles

Our honey company -- Amber Hollow Apiary -- needs new product labels, integrating our new name and logo. We would like one label design that presents equally well on three different sizes of plastic honey bottles. Designs should include a front and back label.

Keep in mind that we really like our old label. Please submit designs that have a similar color and font scheme as the old label.

In the uploaded files, you will find (1) detailed content instructions for each size label (2 lb, 1 lb, 8 oz), (2) photo of three plastic bottles without labels, (3) *.ai file for the new company logo, and (4) image of old package label.

Requirements
Must have
• Same look and feel as our old label, but with our new name and logo

```html
<!DOCTYPE html>
<html lang="en">
<head>
<meta charset="utf-8">
<title>Amber Hollow Apiary – Honey Label Set</title>
<link rel="stylesheet" href="https://fonts.googleapis.com/css2?family=Rye&family=Source+Serif+4:wght@300;400;600;700&family=Arimo:wght@400;700&family=Open+Sans:wght@700&display=swap">
<style>
  :root{
    --backdrop:#f9e9f3;
    --ink:#3a3a32;
    --cream:#faf3de;
    --gold:#c9a227;
    --line:#b89a55;
    --caption:#141414;
  }
  *{box-sizing:border-box;margin:0;padding:0}
  html,body{width:1200px;height:1200px;overflow:hidden}
  body{background:var(--backdrop);position:relative;font-family:"Source Serif 4",Georgia,serif;color:var(--ink)}

  /* ---------- label shell with notched top corners ---------- */
  .label{
    position:absolute;left:var(--x);top:var(--y);width:var(--w);height:var(--h);
    --n:calc(var(--k)*10px);
    --b:calc(var(--k)*5px);
    filter:drop-shadow(1px 2px 2px rgba(0,0,0,.3));
  }
  .label-shape{
    position:absolute;inset:0;background:var(--ink);
    -webkit-mask:
      radial-gradient(circle at 0 0,#0000 var(--n),#000 calc(var(--n) + .5px)),
      radial-gradient(circle at 100% 0,#0000 var(--n),#000 calc(var(--n) + .5px));
    -webkit-mask-composite:source-in;
    mask:
      radial-gradient(circle at 0 0,#0000 var(--n),#000 calc(var(--n) + .5px)),
      radial-gradient(circle at 100% 0,#0000 var(--n),#000 calc(var(--n) + .5px));
    mask-composite:intersect;
  }
  .label-face{
    position:absolute;inset:var(--b);background:var(--cream);
    --nb:calc(var(--n) + var(--b));
    -webkit-mask:
      radial-gradient(circle at calc(var(--b) * -1) calc(var(--b) * -1),#0000 var(--nb),#000 calc(var(--nb) + .5px)),
      radial-gradient(circle at calc(100% + var(--b)) calc(var(--b) * -1),#0000 var(--nb),#000 calc(var(--nb) + .5px));
    -webkit-mask-composite:source-in;
    mask:
      radial-gradient(circle at calc(var(--b) * -1) calc(var(--b) * -1),#0000 var(--nb),#000 calc(var(--nb) + .5px)),
      radial-gradient(circle at calc(100% + var(--b)) calc(var(--b) * -1),#0000 var(--nb),#000 calc(var(--nb) + .5px));
    mask-composite:intersect;
  }

  /* ---------- front ---------- */
  .front .trim{
    position:absolute;left:2%;right:2%;bottom:1.2%;top:3%;
    border:1px solid var(--line);border-top:none;
  }
  .tagline{
    position:absolute;top:4.2%;left:0;right:0;text-align:center;
    font-size:calc(var(--k)*14px);font-weight:300;letter-spacing:calc(var(--k)*.6px);
  }
  .rule{position:absolute;height:1px;background:var(--ink)}
  .rule-top{top:15.8%;left:5.8%;width:48%}
  .rule-low-a{top:38%;left:5.8%;width:21%}
  .rule-low-b{top:38%;left:39%;width:52%}
  .wordmark{
    position:absolute;top:13.2%;left:-6.5%;
    font-family:"Rye",serif;font-size:calc(var(--k)*58px);line-height:1;
    letter-spacing:calc(var(--k)*-2px);white-space:nowrap;color:var(--ink);
    transform:scaleY(1.5);transform-origin:top left;
  }
  .brand-name{
    position:absolute;top:49%;left:6%;width:62%;
    font-size:calc(var(--k)*15px);font-weight:600;line-height:1.1;color:var(--gold);
  }
  .art{
    position:absolute;top:60%;left:13.5%;width:83%;height:33%;
    background:radial-gradient(ellipse at 60% 60%,#c4912a 0%,#dcb765 35%,#efe0b4 70%,rgba(250,243,222,0) 100%);
  }
  .net-weight{
    position:absolute;right:4%;bottom:2.2%;
    font-size:calc(var(--k)*9px);font-weight:400;
  }

  /* ---------- back ---------- */
  .back .label-face{
    display:flex;flex-direction:column;
    padding:calc(var(--k)*22px) calc(var(--k)*11px) calc(var(--k)*8px);
  }
  .promise{
    font-size:calc(var(--k)*12.6px);line-height:1.25;font-weight:300;
    text-align:justify;hyphens:auto;padding:0 calc(var(--k)*4px);
  }
  .nutrition{
    margin-top:calc(var(--k)*12px);
    border:calc(var(--k)*1.6px) solid var(--ink);
    font-family:"Arimo",Arial,sans-serif;
  }
  .nutrition h2{
    background:var(--ink);color:var(--cream);
    font-size:calc(var(--k)*11.5px);font-weight:700;letter-spacing:.3px;
    padding:calc(var(--k)*2px) calc(var(--k)*5px);
  }
  .nutrition ul{list-style:none;padding:calc(var(--k)*8px) calc(var(--k)*8px) calc(var(--k)*4px)}
  .nutrition li{font-size:calc(var(--k)*8.4px);line-height:1.42}
  .nutrition b{font-weight:700}
  .added-sugar{
    display:flex;gap:calc(var(--k)*4px);align-items:flex-start;
    padding:0 calc(var(--k)*8px) calc(var(--k)*8px);
    font-size:calc(var(--k)*6.2px);line-height:1.2;text-align:center;
  }
  .added-sugar svg{flex:none;width:calc(var(--k)*4px);height:calc(var(--k)*10px)}
  .back-footer{
    margin-top:auto;display:flex;justify-content:space-between;align-items:flex-end;
    padding:0 calc(var(--k)*4px);
  }
  .infant-warning{
    font-size:calc(var(--k)*4.4px);font-weight:600;text-transform:uppercase;
    text-align:center;line-height:1.2;margin-bottom:calc(var(--k)*9px);
  }
  .producer{font-size:calc(var(--k)*7.8px);line-height:1.2;text-align:right;font-weight:400}
  .producer strong{font-weight:700;text-transform:uppercase}

  /* ---------- size captions ---------- */
  .size-caption{
    position:absolute;left:0;width:1200px;text-align:center;
    font-family:"Open Sans",Arial,sans-serif;font-weight:700;color:var(--caption);line-height:1.22;
  }
</style>
</head>
<body>

<!-- 8 oz -->
<section class="label front" style="--x:465px;--y:52px;--w:122px;--h:196px;--k:.57">
  <div class="label-shape">
    <div class="label-face">
      <div class="trim"></div>
      <p class="tagline">LOCAL • PURE • RAW</p>
      <span class="rule rule-top"></span>
      <span class="rule rule-low-a"></span><span class="rule rule-low-b"></span>
      <div class="art" role="img" aria-label="Engraved illustration of honeycomb, honey dipper, bee and flowers in gold tones"></div>
      <p class="brand-name">Amber Hollow Apiary</p>
      <p class="net-weight">8 OZ (227g)</p>
    </div>
  </div>
  <p class="wordmark">HONEY</p>
</section>
<section class="label back" style="--x:607px;--y:52px;--w:137px;--h:196px;--k:.55">
  <div class="label-shape">
    <div class="label-face">
      <p class="promise">Amber Hollow Apiary promises 100% pure honey, never pasteurized, and sourced exclusively from beehives we keep near Cedar Hollow, West Virginia”</p>
      <div class="nutrition">
        <h2>Nutrition Facts</h2>
        <ul>
          <li>Servings : 11, <b>Serv. size: 1 Tbsp (21g),</b></li>
          <li>Amount per serving: <b>Calories 60,</b></li>
          <li><b>Total Fat</b> 0g (0% DV), Sat. Fat 0g (0% DV)</li>
          <li>Trans Fat 0g,</li>
          <li><b>Cholest.</b> 0mg (0% DV)</li>
          <li><b>Sodium</b> 0mg (0% DV),</li>
          <li><b>Total Carb.</b> 17g 0mg (6% DV),</li>
          <li>Fiber 0g (0% DV), Total Sugar 17g, 34% DV,</li>
          <li><b>Protein</b> 0g, Vit. D (0% DV), Calcium (0% DV),</li>
          <li>Iron (0% DV), Potas. (0% DV).</li>
        </ul>
        <p class="added-sugar"><svg viewBox="0 0 4 10"><path d="M2 10V1M.3 3L2 0l1.7 3" fill="none" stroke="currentColor" stroke-width=".8"/></svg><span>One serving adds 17g of sugar to your diet and represents 34% of the Daily Value for Added Sugars.</span></p>
      </div>
      <div class="back-footer">
        <p class="infant-warning">“Do not feed honey to<br>infants under one year old”</p>
        <p class="producer"><strong>Amber Hollow Apiary</strong><br>18 Linden Ridge Road<br>Cedar Hollow, WV 25999<br>www.amberhollowapiary.com</p>
      </div>
    </div>
  </div>
</section>
<p class="size-caption" style="top:266px;font-size:19px">SIZE:<br>1.75 inches wide by 2.5 inches</p>

<!-- 1 lb -->
<section class="label front" style="--x:446px;--y:346px;--w:138px;--h:273px;--k:.68">
  <div class="label-shape">
    <div class="label-face">
      <div class="trim"></div>
      <p class="tagline">LOCAL • PURE • RAW</p>
      <span class="rule rule-top"></span>
      <span class="rule rule-low-a"></span><span class="rule rule-low-b"></span>
      <div class="art" role="img" aria-label="Engraved illustration of honeycomb, honey dipper, bee and flowers in gold tones"></div>
      <p class="brand-name">Amber Hollow Apiary</p>
      <p class="net-weight">1 LB (454g)</p>
    </div>
  </div>
  <p class="wordmark">HONEY</p>
</section>
<section class="label back" style="--x:606px;--y:346px;--w:157px;--h:273px;--k:.67">
  <div class="label-shape">
    <div class="label-face">
      <p class="promise">Amber Hollow Apiary promises 100% pure honey, never pasteurized, and sourced exclusively from beehives we keep near Cedar Hollow, West Virginia”</p>
      <div class="nutrition">
        <h2>Nutrition Facts</h2>
        <ul>
          <li>Servings : 22, <b>Serv. size: 1 Tbsp (21g),</b></li>
          <li>Amount per serving: <b>Calories 60,</b></li>
          <li><b>Total Fat</b> 0g (0% DV), Sat. Fat 0g (0% DV)</li>
          <li>Trans Fat 0g,</li>
          <li><b>Cholest.</b> 0mg (0% DV)</li>
          <li><b>Sodium</b> 0mg (0% DV),</li>
          <li><b>Total Carb.</b> 17g 0mg (6% DV),</li>
          <li>Fiber 0g (0% DV), Total Sugar 17g, 34% DV,</li>
          <li><b>Protein</b> 0g, Vit. D (0% DV), Calcium (0% DV),</li>
          <li>Iron (0% DV), Potas. (0% DV).</li>
        </ul>
        <p class="added-sugar"><svg viewBox="0 0 4 10"><path d="M2 10V1M.3 3L2 0l1.7 3" fill="none" stroke="currentColor" stroke-width=".8"/></svg><span>One serving adds 17g of sugar to your diet and represents 34% of the Daily Value for Added Sugars.</span></p>
      </div>
      <div class="back-footer">
        <p class="infant-warning">“Do not feed honey to<br>infants under one year old”</p>
        <p class="producer"><strong>Amber Hollow Apiary</strong><br>18 Linden Ridge Road<br>Cedar Hollow, WV 25999<br>www.amberhollowapiary.com</p>
      </div>
    </div>
  </div>
</section>
<p class="size-caption" style="top:640px;font-size:20px">SIZE:<br>2 inches wide by 3.5 inches</p>

<!-- 2 lb -->
<section class="label front" style="--x:373px;--y:715px;--w:208px;--h:353px;--k:1">
  <div class="label-shape">
    <div class="label-face">
      <div class="trim"></div>
      <p class="tagline">LOCAL • PURE • RAW</p>
      <span class="rule rule-top"></span>
      <span class="rule rule-low-a"></span><span class="rule rule-low-b"></span>
      <div class="art" role="img" aria-label="Engraved illustration of honeycomb, honey dipper, bee and flowers in gold tones"></div>
      <p class="brand-name">Amber Hollow Apiary</p>
      <p class="net-weight">2 LB (907g)</p>
    </div>
  </div>
  <p class="wordmark">HONEY</p>
</section>
<section class="label back" style="--x:605px;--y:715px;--w:235px;--h:353px;--k:1">
  <div class="label-shape">
    <div class="label-face">
      <p class="promise">Amber Hollow Apiary promises 100% pure honey, never pasteurized, and sourced exclusively from beehives we keep near Cedar Hollow, West Virginia”</p>
      <div class="nutrition">
        <h2>Nutrition Facts</h2>
        <ul>
          <li>Servings : 43, <b>Serv. size: 1 Tbsp (21g),</b></li>
          <li>Amount per serving: <b>Calories 60,</b></li>
          <li><b>Total Fat</b> 0g (0% DV), Sat. Fat 0g (0% DV)</li>
          <li>Trans Fat 0g,</li>
          <li><b>Cholest.</b> 0mg (0% DV)</li>
          <li><b>Sodium</b> 0mg (0% DV),</li>
          <li><b>Total Carb.</b> 17g 0mg (6% DV),</li>
          <li>Fiber 0g (0% DV), Total Sugar 17g, 34% DV,</li>
          <li><b>Protein</b> 0g, Vit. D (0% DV), Calcium (0% DV),</li>
          <li>Iron (0% DV), Potas. (0% DV).</li>
        </ul>
        <p class="added-sugar"><svg viewBox="0 0 4 10"><path d="M2 10V1M.3 3L2 0l1.7 3" fill="none" stroke="currentColor" stroke-width=".8"/></svg><span>One serving adds 17g of sugar to your diet and represents 34% of the Daily Value for Added Sugars.</span></p>
      </div>
      <div class="back-footer">
        <p class="infant-warning">“Do not feed honey to<br>infants under one year old”</p>
        <p class="producer"><strong>Amber Hollow Apiary</strong><br>18 Linden Ridge Road<br>Cedar Hollow, WV 25999<br>www.amberhollowapiary.com</p>
      </div>
    </div>
  </div>
</section>
<p class="size-caption" style="top:1084px;font-size:27px">SIZE:<br>3 inches wide by 4.5 inches</p>

</body>
</html>
```